Business Card

We need some ideas for corporate business cards. I'm interested in a double sided card, with one side featuring our corporate logo, the other side with employee information.

Corporate colors, logo etc. available at www.brivalo.com

Industry/Entity Type

Business

Requirements
Must have
• The "Brivalo" logo with stylized "O"

Nice to have
• Preferred font is calibri

```html
<!DOCTYPE html>
<html lang="en">
<head>
<meta charset="utf-8">
<title>Brivalo Business Card</title>
<link rel="stylesheet" href="https://fonts.googleapis.com/css2?family=Carlito:ital,wght@0,400;0,700;1,400;1,700&display=swap">
<style>
  :root {
    --brand-blue: #536a9a;
    --paper: #ffffff;
    --ink: #2f2f2f;
    --ink-soft: #444444;
    --rule: #555555;
    --link: #1a0dab;
    --stage: #ecebe8;
    --pm: #7a1f3d;
    --ig: #e58a2c;
    --sg: #1f6b6b;
    --um: #5b82b8;
  }
  * { box-sizing: border-box; margin: 0; padding: 0; }
  html, body { width: 1200px; height: 1000px; overflow: hidden; }
  body {
    background: var(--stage);
    font-family: "Carlito", "Calibri", sans-serif;
    position: relative;
  }
  .card {
    position: absolute;
    left: 190px;
    width: 820px;
    height: 466px;
    overflow: hidden;
  }
  .card--front { top: 22px; background: var(--paper); }
  .card--back { top: 512px; background: var(--brand-blue); }

  /* front header */
  .card__header {
    position: absolute; left: 0; top: 0; width: 100%; height: 106px;
    background: var(--brand-blue);
    text-align: center; color: var(--paper);
  }
  .brand {
    display: inline-flex; align-items: center; gap: 12px;
    margin-top: 16px;
    font-weight: 700; letter-spacing: 6px; text-transform: uppercase;
  }
  .brand__mark { display: inline-block; background: var(--paper); }
  .card__header .brand { font-size: 48px; line-height: 50px; }
  .card__header .brand__mark { width: 34px; height: 34px; }
  .tagline { font-style: italic; font-size: 14px; margin-top: 8px; }

  /* front body */
  .person { position: absolute; left: 90px; top: 225px; color: var(--ink); }
  .person__name { font-size: 27px; }
  .person__role { font-size: 24px; font-weight: 700; font-style: italic; margin-top: 8px; }
  .divider {
    position: absolute; left: 441px; top: 175px; width: 2px; height: 178px;
    background: var(--rule);
  }
  .contacts { position: absolute; left: 461px; top: 180px; color: var(--ink-soft); font-size: 20px; line-height: 28px; }
  .contacts__title { color: var(--brand-blue); font-weight: 700; font-size: 24px; line-height: 24px; }
  .contacts b { color: var(--ink); }
  .contacts a { color: var(--link); }

  /* products bar */
  .products-tab {
    position: absolute; left: 0; top: 405px; width: 76px; height: 12px;
    background: var(--brand-blue); color: var(--paper);
    font-size: 11px; line-height: 12px; padding-left: 10px;
  }
  .products {
    position: absolute; left: 0; bottom: 0; width: 100%; height: 49px;
    background: var(--brand-blue);
    display: flex; align-items: center; justify-content: space-around; padding: 0 10px;
    list-style: none; color: var(--paper); font-size: 17px;
    font-family: "Arial", sans-serif;
  }
  .product { display: flex; align-items: center; gap: 8px; }
  .product__badge {
    width: 28px; height: 28px; border: 1.5px solid #d8deea;
    font-size: 10px; font-weight: 700; display: flex; align-items: center; justify-content: center;
  }
  .product__badge--pm { background: var(--pm); }
  .product__badge--ig { background: var(--ig); }
  .product__badge--sg { background: var(--sg); }
  .product__badge--um { background: var(--um); }

  /* back */
  .card--back .brand {
    position: absolute; left: 50%; top: 50%; transform: translate(-50%, -50%);
    margin: 0; color: var(--paper); font-size: 100px; line-height: 100px; letter-spacing: 12px; gap: 24px;
  }
  .card--back .brand__mark { width: 64px; height: 64px; }
</style>
</head>
<body>
  <section class="card card--front" aria-label="Card front with employee information">
    <header class="card__header">
      <div class="brand"><span class="brand__mark"></span>Brivalo</div>
      <p class="tagline">Brivalo technology delivers insight, control, monetization, and interaction to the world's largest network operators</p>
    </header>
    <div class="person">
      <p class="person__name">M.r Halden</p>
      <p class="person__role">Marketing Manager</p>
    </div>
    <div class="divider"></div>
    <div class="contacts">
      <p class="contacts__title">CONTACTS:</p>
      <p><b>Phone:</b> +1 47-2206 18</p>
      <p><b>Mobile:</b> +553104 9</p>
      <p><b>Email:</b> <a href="mailto:halden@brivalo.com">halden@brivalo.com</a></p>
      <p><b>FB:</b> Brivalo</p>
      <p><b>Box:</b> 42 18, Marlow strt, Easton City.</p>
    </div>
    <div class="products-tab">Products</div>
    <ul class="products">
      <li class="product"><span class="product__badge product__badge--pm">PM</span>Policy charging</li>
      <li class="product"><span class="product__badge product__badge--ig">IG</span>Evolved charging</li>
      <li class="product"><span class="product__badge product__badge--sg">SG</span>Signal Gateway</li>
      <li class="product"><span class="product__badge product__badge--um">UM</span>Unified Mediation</li>
    </ul>
  </section>

  <section class="card card--back" aria-label="Card back with company name">
    <div class="brand"><span class="brand__mark"></span>Brivalo</div>
  </section>
</body>
</html>
```